Indoor Gun Range Web Design Project

Create a professional bold indoor gun range website. Logo colors are white, red, and black. This is a very professional gun range. Please use high quality stock images if possible. Stay away from a lot of militia type photos. Use your best judgement on what to put as a main image and headline.

Here are some websites that I like for design.

http://www.pinebrookarsenal.example/
http://www.layoutbazaar.example/website-templates/51947.html
http://www.marigoldworks.example/

Target Market(s)

Men ages 25-65

Industry/Entity Type

Gun

Requirements
Must have
• Bold lettering, logo attached, exciting photos.
Should not have
• A lot of militia photos.

```html
<!DOCTYPE html>
<html lang="en">
<head>
<meta charset="utf-8">
<title>News – True Mark Indoor Range</title>
<link rel="stylesheet" href="https://fonts.googleapis.com/css2?family=Anton&family=Oswald:wght@500&family=Alegreya+Sans+SC:wght@700;800&display=swap">
<style>
  :root {
    --red: #d0202a;
    --red-dark: #a8141c;
    --black: #0a0a0a;
    --white: #ffffff;
    --text: #111111;
  }
  * { box-sizing: border-box; margin: 0; padding: 0; }
  html, body { width: 1200px; height: 928px; overflow: hidden; background: var(--white); }
  .page { position: relative; width: 1200px; height: 928px; overflow: hidden; background: var(--white); font-family: "Alegreya Sans SC", sans-serif; }

  .site-header { position: absolute; left: 0; top: 0; width: 1200px; height: 123px;
    background: linear-gradient(90deg, #e6e6e6 0%, #f7f7f7 40%, #d8d8d8 64%, var(--white) 64.2%); }
  .page-title { position: absolute; left: 12px; top: 14px; font-family: "Anton", sans-serif;
    font-size: 86px; line-height: 1; color: var(--black); letter-spacing: 1px; }
  .brand { position: absolute; right: 22px; top: 34px; display: flex; align-items: center; gap: 12px; white-space: nowrap; }
  .brand-name { font-family: "Alegreya Sans SC", sans-serif; font-weight: 800; color: var(--red);
    font-size: 27px; line-height: 1; letter-spacing: 0.5px; white-space: nowrap; }
  .brand-dot { flex: none; width: 54px; height: 54px; border-radius: 50%; border: 4px solid var(--red); }

  .band { position: absolute; left: 0; width: 1200px; }
  .band-red-top { top: 123px; height: 9px; background: var(--red); }
  .band-black-top { top: 140px; height: 11px; background: var(--black); }
  .band-black-bottom { top: 873px; height: 15px; background: var(--black); }
  .band-red-bottom { top: 894px; height: 16px; background: var(--red); }
  .band-grey-bottom { top: 910px; height: 18px; background: linear-gradient(90deg, #cfcfcf, #f4f4f4, #cfcfcf); }

  .main-nav { position: absolute; left: 28px; top: 172px; width: 146px; }
  .main-nav a { display: block; height: 34px; margin-bottom: 15px; text-align: center; text-decoration: none;
    font-family: "Oswald", sans-serif; font-weight: 500; font-size: 22px; line-height: 34px;
    color: var(--red); background: linear-gradient(180deg, #fafafa 0%, #cfcfcf 55%, #e9e9e9 100%); }
  .main-nav a.is-current { color: var(--black); }

  .photo { position: absolute; }
  .photo-rack { left: 28px; top: 469px; width: 146px; height: 373px;
    background: linear-gradient(135deg, #e8e4dc 0%, #a8a49c 45%, #4a4844 75%, #d6d2ca 100%); }
  .photo-shooter-lane { left: 197px; top: 607px; width: 315px; height: 235px;
    background: linear-gradient(160deg, #1c2a28 0%, #3b4a44 45%, #b9a58a 75%, #4f6a3e 100%); }
  .photo-shooter-booth { left: 530px; top: 189px; width: 314px; height: 214px;
    background: linear-gradient(110deg, #d8d4cc 0%, #b38a5c 35%, #2a2624 60%, #c8c4bc 100%); }
  .photo-target { left: 863px; top: 607px; width: 315px; height: 235px;
    background: radial-gradient(ellipse at 50% 70%, #d8d8d8 0%, #8a8a8a 30%, #1a1a1a 55%, #f0f0f0 80%); }

  .news-card { position: absolute; width: 315px; padding: 26px 18px 0;
    background: linear-gradient(180deg, #e4e4e4 0%, var(--white) 35%, #b8b8b8 100%); text-align: center; }
  .news-card-1 { left: 197px; top: 155px; height: 437px; }
  .news-card-2 { left: 530px; top: 416px; height: 457px; padding-top: 14px; }
  .news-card-3 { left: 863px; top: 155px; height: 437px; }
  .news-title { font-family: "Alegreya Sans SC", sans-serif; font-weight: 800; color: var(--red);
    font-size: 21px; letter-spacing: 2px; margin-bottom: 18px; }
  .news-body { font-weight: 700; font-size: 14.5px; line-height: 17px; color: var(--text); letter-spacing: 0.4px; }
  .news-disclaimer { font-weight: 700; font-size: 10px; line-height: 14px; color: var(--red-dark);
    margin-top: 24px; padding: 0 6px; letter-spacing: 0.3px; }
</style>
</head>
<body>
<div class="page">
  <header class="site-header">
    <h1 class="page-title">NEWS</h1>
    <div class="brand">
      <span class="brand-name">TRUE MARK INDOOR RANGE</span>
      <span class="brand-dot"></span>
    </div>
  </header>
  <div class="band band-red-top"></div>
  <div class="band band-black-top"></div>

  <nav class="main-nav">
    <a href="#">HOME</a>
    <a href="#">FEES</a>
    <a href="#">RULES</a>
    <a href="#" class="is-current">NEWS</a>
    <a href="#">MEMBERSHIP</a>
    <a href="#">CONTACT</a>
  </nav>

  <div class="photo photo-rack" role="img" aria-label="Handguns displayed on a rack"></div>

  <article class="news-card news-card-1">
    <h2 class="news-title">NEWS 1</h2>
    <p class="news-body">your text here - Hey ladies! Why let the guys have all the fun? Monday is dedicated to you! Every Monday at True Mark Indoor Range ladies get to shoot for free! We'll waive your lane fee or guest pass and supply a couple T2 targets so you have something to shoot at! We'll even give you a little assistance if you're a new shooter or just want some pointers on how to shoot better.<br>If you're not a current Lakemont Gun Club member we'll waive the membership fee for your first 3 visits. A signed waiver of liability and rule sheet are required for all participants.</p>
    <p class="news-disclaimer">Disclaimer: This offer is valid during regular Monday business hours and excludes gun rental, ammo and extra targets.</p>
  </article>
  <div class="photo photo-shooter-lane" role="img" aria-label="Shooter firing a handgun down a range lane"></div>

  <div class="photo photo-shooter-booth" role="img" aria-label="Woman with ear protection aiming in a shooting booth"></div>
  <article class="news-card news-card-2">
    <h2 class="news-title">NEWS 2</h2>
    <p class="news-body">your text here - Hey ladies! Why let the guys have all the fun? Monday is dedicated to you! Every Monday at True Mark Indoor Range ladies get to shoot for free! We'll waive your lane fee or guest pass and supply a couple T2 targets so you have something to shoot at! We'll even give you a little assistance if you're a new shooter or just want some pointers on how to shoot better.<br>If you're not a current Lakemont Gun Club member we'll waive the membership fee for your first 3 visits. A signed waiver of liability and rule sheet are required for all participants.</p>
    <p class="news-disclaimer">Disclaimer: This offer is valid during regular Monday business hours and excludes gun rental, ammo and extra targets.</p>
  </article>

  <article class="news-card news-card-3">
    <h2 class="news-title">NEWS 3</h2>
    <p class="news-body">your text here - Hey ladies! Why let the guys have all the fun? Monday is dedicated to you! Every Monday at True Mark Indoor Range ladies get to shoot for free! We'll waive your lane fee or guest pass and supply a couple T2 targets so you have something to shoot at! We'll even give you a little assistance if you're a new shooter or just want some pointers on how to shoot better.<br>If you're not a current Lakemont Gun Club member we'll waive the membership fee for your first 3 visits. A signed waiver of liability and rule sheet are required for all participants.</p>
    <p class="news-disclaimer">Disclaimer: This offer is valid during regular Monday business hours and excludes gun rental, ammo and extra targets.</p>
  </article>
  <div class="photo photo-target" role="img" aria-label="Paper silhouette target with bullet holes"></div>

  <div class="band band-black-bottom"></div>
  <div class="band band-red-bottom"></div>
  <div class="band band-grey-bottom"></div>
</div>
</body>
</html>
```